Postcard Project

I need a postcard designed 6X9 in size printed full color
Will need in the end a high resolution print ready file with crop marks
See instructions in word doc

```html
<!DOCTYPE html>
<html lang="en">
<head>
<meta charset="utf-8">
<title>Drinkware Postcard</title>
<link rel="stylesheet" href="https://fonts.googleapis.com/css2?family=Oswald:wght@500&family=Poppins:wght@400;500;600;700;800&display=swap">
<style>
  :root {
    --navy: #173a66;
    --brand-blue: #1f5cb0;
    --ink: #1d1d1f;
    --white: #ffffff;
    --sky-light: #f4f4f6;
    --sky-mid: #dcdde2;
    --wood-light: #e3cba8;
    --wood-dark: #4e3d2c;
  }
  * { margin: 0; padding: 0; box-sizing: border-box; }
  html, body { width: 1200px; height: 1200px; overflow: hidden; }
  body {
    background: var(--navy);
    font-family: "Poppins", sans-serif;
    position: relative;
  }
  .card {
    position: absolute;
    left: 217px;
    width: 765px;
    height: 511px;
    overflow: hidden;
    box-shadow: 0 4px 18px rgba(0,0,0,0.35);
  }
  .card--front {
    top: 65px;
    background: radial-gradient(ellipse at 50% 45%, var(--white) 0%, var(--sky-light) 45%, var(--sky-mid) 100%);
  }
  .card--back { top: 624px; background: var(--white); }
  .abs { position: absolute; }

  /* Front */
  .front-title {
    left: 0; width: 100%; top: 24px; text-align: center;
    font-weight: 700; font-size: 58px; letter-spacing: 0.3px;
    color: var(--brand-blue); line-height: 1;
  }
  .badge { left: 75px; top: 94px; width: 160px; height: 160px; overflow: visible; }
  .badge-number { font-family: "Oswald", sans-serif; font-weight: 500; fill: var(--white); }
  .badge-off { font-family: "Poppins", sans-serif; font-weight: 700; fill: var(--white); }
  .offer-headline {
    left: 245px; top: 112px;
    font-weight: 600; font-size: 29px; line-height: 35px;
    color: var(--brand-blue); letter-spacing: 0.2px;
  }
  .promo-pill {
    position: absolute; height: 36px; border-radius: 18px;
    background: var(--brand-blue); color: var(--white);
    font-size: 19.5px; font-weight: 400; line-height: 36px;
    text-align: center; white-space: nowrap;
  }
  .promo-pill strong { font-weight: 700; }
  .promo-pill--drink { left: 245px; top: 193px; width: 241px; }
  .expiry {
    left: 498px; top: 200px;
    font-size: 17px; color: var(--ink); line-height: 22px;
  }
  .product-photo {
    left: 0; top: 240px; width: 765px; height: 271px;
    background: linear-gradient(180deg, rgba(236,236,240,0) 0%, rgba(230,228,226,0.6) 30%, var(--wood-light) 62%, #c9ad88 76%, var(--wood-dark) 100%);
  }

  /* Back */
  .refer-kicker {
    left: 33px; top: 30px;
    font-weight: 700; font-size: 28px; line-height: 1; color: var(--brand-blue);
  }
  .refer-headline {
    left: 32px; top: 62px;
    font-weight: 700; font-size: 38px; line-height: 1; color: var(--brand-blue);
  }
  .refer-body {
    left: 33px; top: 106px; width: 380px;
    font-size: 16.5px; line-height: 20px; color: var(--ink);
  }
  .refer-body .gap { display: block; margin-top: 8px; }
  .promo-pill--refer { left: 34px; top: 196px; width: 233px; }
  .divider {
    left: 33px; top: 267px; width: 351px; height: 2px; background: var(--brand-blue);
  }
  .first-headline {
    left: 33px; top: 300px;
    font-weight: 700; font-size: 37px; line-height: 1; color: var(--brand-blue);
  }
  .first-body {
    left: 34px; top: 344px;
    font-size: 16.5px; line-height: 22px; color: var(--ink);
  }
  .promo-pill--first { left: 34px; top: 385px; width: 263px; }
  .fine-print {
    left: 33px; top: 462px;
    font-size: 16.5px; line-height: 22px; color: var(--ink);
  }
  .stamp-box { left: 627px; top: 32px; width: 107px; height: 86px; }
  .address-box { left: 393px; top: 308px; width: 341px; height: 172px; }
</style>
</head>
<body>

  <section class="card card--front">
    <h1 class="abs front-title">DRINKWARE</h1>

    <svg class="abs badge" viewBox="0 0 160 160" aria-label="50% off">
      <polygon fill="var(--brand-blue)" stroke="var(--white)" stroke-width="5" stroke-linejoin="round"
        points="152,80 139.9,96.1 142.4,116 123.8,123.8 116,142.4 96.1,139.9 80,152 63.9,139.9 44,142.4 36.2,123.8 17.6,116 20.1,96.1 8,80 20.1,63.9 17.6,44 36.2,36.2 44,17.6 63.9,20.1 80,8 96.1,20.1 116,17.6 123.8,36.2 142.4,44 139.9,63.9"/>
      <text class="badge-number" x="30" y="114" font-size="78" textLength="57" lengthAdjust="spacingAndGlyphs">50</text>
      <text class="badge-number" x="91" y="93" font-size="52" textLength="42" lengthAdjust="spacingAndGlyphs">%</text>
      <text class="badge-off" x="91" y="114" font-size="21" textLength="41" lengthAdjust="spacingAndGlyphs">OFF</text>
    </svg>

    <p class="abs offer-headline">ON YOUR<br>DRINKWARE ORDER OVER $500</p>
    <div class="promo-pill promo-pill--drink">PROMO CODE: <strong>DRINK</strong></div>
    <p class="abs expiry">Good till 9/30/25</p>

    <div class="abs product-photo" role="img" aria-label="Photo of branded tumblers, mugs, cups and bottles in white, silver, red, blue and black standing on a round wooden table"></div>
  </section>

  <section class="card card--back">
    <h2 class="abs refer-kicker">REFER TO A FRIEND</h2>
    <p class="abs refer-headline">GIVE $100, GET $100</p>
    <p class="abs refer-body">Give your friends $100 off their first purchase<span class="gap">(over $500) and receive a $100 discount</span>on any order (over $500).</p>
    <div class="promo-pill promo-pill--refer">PROMO CODE: <strong>REFER</strong></div>

    <div class="abs divider"></div>

    <h2 class="abs first-headline">$150 OFF</h2>
    <p class="abs first-body">Your first department purchase of $500</p>
    <div class="promo-pill promo-pill--first">PROMO CODE: <strong>FIRST150</strong></div>

    <p class="abs fine-print">*Promotions cannot be combined</p>

    <svg class="abs stamp-box" viewBox="0 0 107 86" aria-hidden="true">
      <rect x="1" y="1" width="105" height="84" fill="none" stroke="var(--brand-blue)" stroke-width="1.5" stroke-dasharray="12 9"/>
    </svg>
    <svg class="abs address-box" viewBox="0 0 341 172" aria-hidden="true">
      <rect x="1" y="1" width="339" height="170" fill="none" stroke="var(--brand-blue)" stroke-width="1.5" stroke-dasharray="14 9"/>
    </svg>
  </section>

</body>
</html>
```